Cascade Rhythm Guild Business Cards

The Cascade Rhythm Guild is a non-profit organization that supports, promotes, and manages music events in the Pacific Northwest. Our mission is to keep the blues alive. We do this by partnering with local venues, schools, and national acts to bring some of the best blues music to our members. As newly elected Executive Board Members we would like to have new business cards designed. I have included a copy of our logo.

```html
<!DOCTYPE html>
<html lang="en">
<head>
<meta charset="utf-8">
<title>Cascade Rhythm Guild Business Cards</title>
<link href="https://fonts.googleapis.com/css2?family=Montserrat:wght@700;800&family=Lato:wght@400&display=swap" rel="stylesheet">
<style>
  :root {
    --backdrop: #a3a3a3;
    --blue-deep: #1f506c;
    --blue-light: #33708f;
    --cream: #f3ee8e;
    --red: #b71c1c;
    --ink: #1f1f1f;
    --wood-dark: #3a1f1c;
    --wood-mid: #5a2d28;
  }
  * { margin: 0; padding: 0; box-sizing: border-box; }
  html, body { width: 1200px; height: 1000px; overflow: hidden; }
  body { background: var(--backdrop); position: relative; font-family: 'Lato', sans-serif; }

  .card {
    position: absolute; left: 186px; width: 828px; height: 472px;
    border-radius: 18px; overflow: hidden;
  }
  .card--front { top: 17px; background: radial-gradient(ellipse at 50% 45%, var(--blue-light) 0%, var(--blue-deep) 75%); }
  .card--back { top: 505px; background: var(--cream); }

  .brand { position: absolute; display: flex; align-items: center; gap: 18px; }
  .brand__dot { border-radius: 50%; flex: none; }
  .brand__name {
    font-family: 'Montserrat', sans-serif; font-weight: 800; line-height: 1.05;
    text-transform: uppercase; letter-spacing: 1px;
  }
  .card--front .brand { left: 0; right: 0; top: 196px; justify-content: center; }
  .card--front .brand__dot { width: 84px; height: 84px; background: var(--cream); }
  .card--front .brand__name { color: var(--cream); font-size: 38px; }

  .card--back .brand { left: 38px; top: 212px; gap: 14px; }
  .card--back .brand__dot { width: 56px; height: 56px; background: var(--red); }
  .card--back .brand__name { color: var(--red); font-size: 28px; }

  .person { position: absolute; left: 384px; top: 105px; }
  .person__name { font-family: 'Montserrat', sans-serif; font-weight: 700; font-size: 35px; color: var(--red); letter-spacing: 0.5px; line-height: 1; }
  .person__role { font-size: 20px; color: var(--ink); margin-top: 6px; }

  .contacts { position: absolute; left: 386px; top: 208px; list-style: none; }
  .contacts__item { display: flex; align-items: flex-start; gap: 13px; font-size: 21px; color: var(--ink); line-height: 30px; margin-bottom: 5px; }
  .contacts__item--address { margin-top: 8px; }
  .contacts__icon { width: 26px; height: 26px; flex: none; margin-top: 2px; }

  .guitar-art {
    position: absolute; left: 662px; top: 15px; width: 166px; height: 457px;
    border-radius: 14px 0 0 0;
    background: linear-gradient(180deg, rgba(90,45,40,0.15) 0%, rgba(90,45,40,0.55) 55%, var(--wood-dark) 100%);
  }
</style>
</head>
<body>
  <section class="card card--front">
    <div class="brand">
      <span class="brand__dot"></span>
      <span class="brand__name">Cascade Rhythm<br>Guild</span>
    </div>
  </section>

  <section class="card card--back">
    <div class="brand">
      <span class="brand__dot"></span>
      <span class="brand__name">Cascade<br>Rhythm Guild</span>
    </div>

    <div class="person">
      <h1 class="person__name">MARA ELLISON</h1>
      <p class="person__role">Music Event Manager</p>
    </div>

    <ul class="contacts">
      <li class="contacts__item">
        <svg class="contacts__icon" viewBox="0 0 26 26"><rect x="1" y="1" width="24" height="24" rx="4" fill="none" stroke="#b71c1c" stroke-width="2"/><path d="M8 7c1-1 2 0 3 2s-1 2 0 4 2 3 4 2 2 2 1 3-5 1-7-3-2-7-1-8z" fill="#b71c1c"/></svg>
        <span>044-987 654 321</span>
      </li>
      <li class="contacts__item">
        <svg class="contacts__icon" viewBox="0 0 26 26"><rect x="1" y="1" width="24" height="24" rx="4" fill="none" stroke="#b71c1c" stroke-width="2"/><path d="M6 13l14-6-5 14-3-5z" fill="#b71c1c"/></svg>
        <span>info@cascaderhythm.org</span>
      </li>
      <li class="contacts__item">
        <svg class="contacts__icon" viewBox="0 0 26 26"><rect x="1" y="1" width="24" height="24" rx="4" fill="none" stroke="#b71c1c" stroke-width="2"/><circle cx="13" cy="13" r="7" fill="none" stroke="#b71c1c" stroke-width="1.6"/><path d="M6 13h14M13 6c-3 4-3 10 0 14M13 6c3 4 3 10 0 14" fill="none" stroke="#b71c1c" stroke-width="1.3"/></svg>
        <span>www.cascaderhythm.org</span>
      </li>
      <li class="contacts__item contacts__item--address">
        <svg class="contacts__icon" viewBox="0 0 26 26"><rect x="1" y="1" width="24" height="24" rx="4" fill="none" stroke="#b71c1c" stroke-width="2"/><path d="M13 21s-6-6-6-10a6 6 0 0112 0c0 4-6 10-6 10z" fill="#b71c1c"/><circle cx="13" cy="11" r="2.2" fill="#f3ee8e"/></svg>
        <span>4410 Harbor Ridge Rd,<br>212-B, WA 98101</span>
      </li>
    </ul>

    <div class="guitar-art" role="img" aria-label="Illustration of an acoustic guitar standing upright"></div>
  </section>
</body>
</html>
```